【依頼の目的/概要】
電子書籍(vellis)の表紙デザインをお願いします。

【画像サイズ】 ※VSRより抜粋
表紙ファイルの理想的な寸法 2,560×1,600ピクセルです。
注:画像の寸法は 1,000×625ピクセル以上であることが必要です。
画像の最大の寸法は 10,000×10,000ピクセルです。

【タイトル】

港町の料理人へ贈る
季節ごとに変わる庭の手入れがわかる
「月灯り菜園ノート」

【著者】

MIRO

【本の内容】

5つの窓辺・ロカルナ年代記などの人間心理・成功本から
パートナーに関する知識をまとめて解説した本です。

※本文を参考資料として添付します。

【デザイン要望】

特にイメージにこだわりはありませんので、
自由な発送でのデザインご応募を楽しみにしています。

※次点、次々点の方への参加報酬を設定致しました。

※その他 必要な情報がありましたら、お問い合わせください。

ターゲット層がリアル風が好きだと思ったので、選びました

今回も多数応募頂きまして、誠にありがとうございました。

```html
<!DOCTYPE html>
<html lang="ja">
<head>
<meta charset="utf-8">
<title>月灯り菜園ノート</title>
<link rel="stylesheet" href="https://fonts.googleapis.com/css2?family=Noto+Sans+JP:wght@500;700;900&family=Caveat:wght@700&display=swap">
<style>
  :root {
    --navy: #1f3d70;
    --cream: #fbf0d9;
    --pale-blue: #d3e5f3;
    --sky: #9cc4e4;
    --yellow: #f4d46a;
    --white: #ffffff;
  }
  * { margin: 0; padding: 0; box-sizing: border-box; }
  html, body { width: 750px; height: 1200px; overflow: hidden; background: var(--cream); }
  .cover {
    position: relative; width: 750px; height: 1200px; overflow: hidden;
    background: var(--cream);
    font-family: "Noto Sans JP", sans-serif; color: var(--navy);
  }
  .bg-shape { position: absolute; left: 0; top: 0; }
  .top-band {
    position: absolute; left: 0; top: 0; width: 750px; height: 98px;
    background: var(--navy); color: var(--white);
    display: flex; align-items: center; justify-content: center;
    font-weight: 700; font-size: 40px; letter-spacing: 4px;
  }
  .lead-bubble { position: absolute; left: 270px; top: 108px; }
  .lead-text {
    position: absolute; left: 270px; top: 128px; width: 350px;
    text-align: center; font-weight: 900; font-size: 38px; line-height: 1.25;
  }
  .title-word { position: absolute; font-weight: 900; line-height: 1; white-space: nowrap; }
  .title-small { left: 95px; top: 210px; font-size: 66px; }
  .title-main-1 { left: 95px; top: 300px; font-size: 150px; letter-spacing: 4px; }
  .title-main-2 { left: 95px; top: 455px; font-size: 140px; letter-spacing: 2px; }
  .title-tail { left: 520px; top: 530px; font-size: 54px; }
  .title-deco {
    position: absolute; left: 160px; top: 330px;
    font-family: "Caveat", cursive; font-size: 130px; color: var(--navy);
    opacity: 0.12; transform: rotate(12deg); letter-spacing: 6px; white-space: nowrap;
  }
  .scene-art {
    position: absolute; left: 20px; top: 620px; width: 710px; height: 290px;
    border-radius: 50% / 40%;
    background: radial-gradient(ellipse at center, var(--pale-blue) 0%, #e6eef2 65%, var(--cream) 100%);
  }
  .footer-band { position: absolute; left: 0; top: 880px; }
  .leaf-left, .leaf-right {
    position: absolute; background: linear-gradient(160deg, var(--sky), var(--pale-blue));
    opacity: 0.85;
  }
  .leaf-left { left: -20px; top: 950px; width: 200px; height: 270px; border-radius: 60% 40% 0 0; }
  .leaf-right { left: 560px; top: 975px; width: 210px; height: 240px; border-radius: 45% 55% 0 0; }
  .limited-tag {
    position: absolute; left: 230px; top: 912px; padding: 4px 16px;
    background: var(--yellow); color: var(--navy); font-weight: 900; font-size: 26px;
    border-radius: 8px; transform: rotate(-8deg);
  }
  .gift-title {
    position: absolute; left: 200px; top: 960px; width: 300px; text-align: center;
    color: var(--white); font-weight: 900; font-size: 38px;
  }
  .gift-icon { position: absolute; left: 500px; top: 955px; }
  .gift-desc {
    position: absolute; left: 150px; top: 1015px; width: 450px; text-align: center;
    color: var(--white); font-weight: 700; font-size: 30px; line-height: 1.3;
  }
  .author {
    position: absolute; left: 0; top: 1098px; width: 750px; text-align: center;
    color: var(--yellow); font-weight: 900; font-size: 42px; letter-spacing: 2px;
  }
</style>
</head>
<body>
<main class="cover">
  <svg class="bg-shape" width="750" height="700" viewBox="0 0 750 700" aria-hidden="true">
    <path d="M0 98 H460 C430 180 300 240 160 250 C90 255 30 240 0 225 Z" fill="#e4ecef"/>
  </svg>

  <header class="top-band">港町の料理人へ贈る</header>

  <svg class="lead-bubble" width="360" height="150" viewBox="0 0 360 150" aria-hidden="true">
    <path d="M20 4 H340 Q356 4 356 20 V112 Q356 128 340 128 H90 L60 146 L64 128 H20 Q4 128 4 112 V20 Q4 4 20 4 Z"
          fill="#ffffff" stroke="#9cc4e4" stroke-width="4"/>
  </svg>
  <p class="lead-text">季節ごとに変わる<br>庭の手入れがわかる</p>

  <div class="title-deco" aria-hidden="true">MOONLIGHT</div>
  <h1>
    <span class="title-word title-small">月灯り</span>
    <span class="title-word title-main-1">菜園</span>
    <span class="title-word title-main-2">ノート</span>
  </h1>

  <div class="scene-art" role="img" aria-label="テーブルを囲んでノートパソコンやタブレットで話し合う三人のイラスト"></div>

  <svg class="footer-band" width="750" height="320" viewBox="0 0 750 320" aria-hidden="true">
    <path d="M0 40 C180 0 560 0 750 40 V320 H0 Z" fill="#1f3d70"/>
  </svg>
  <div class="leaf-left" role="img" aria-label="水色の葉のイラスト"></div>
  <div class="leaf-right" role="img" aria-label="水色の葉のイラスト"></div>

  <section class="gift">
    <div class="limited-tag">本書限定</div>
    <p class="gift-title">無料プレゼント</p>
    <svg class="gift-icon" width="56" height="56" viewBox="0 0 56 56" aria-hidden="true">
      <g fill="none" stroke="#ffffff" stroke-width="3">
        <rect x="6" y="20" width="44" height="10"/>
        <rect x="10" y="30" width="36" height="22"/>
        <line x1="28" y1="20" x2="28" y2="52"/>
        <path d="M28 20 C20 6 10 12 18 20 M28 20 C36 6 46 12 38 20"/>
      </g>
    </svg>
    <p class="gift-desc">『あなたのパーソナリティ分析』<br>についてまとめたテスト</p>
  </section>

  <p class="author">MIRO 著</p>
</main>
</body>
</html>
```